Real Estate Flyer

I would like an A4 size flyer which has the same info 3 times and can be cut into three.
It will be used for letterbox drops for new listings (SELLING) and sold listings (SOLD). The flyer needs a heading (as above) and a space for a photo which is able to be changed for each new property. Needs to be blue, red and white. It also requires my photo, KLT logo, Marisse Thornbury logo and the following text:
"Are you considering selling? Call Marisse today for a complimentary market appraisal".
(KLT logo, Marisse Thornbury Sales Consultant logo and my photo can be found in uploaded files)
Industry/Entity Type
Real Estate
Look and feel

```html
<!DOCTYPE html>
<html lang="en">
<head>
<meta charset="utf-8">
<title>KLT Homelink – Marisse Thornbury Flyer</title>
<link rel="stylesheet" href="https://fonts.googleapis.com/css2?family=Open+Sans:wght@400;600&family=Tinos:wght@700&display=swap">
<style>
  :root {
    --red: #d21f1c;
    --navy: #15295b;
    --mist: #ededed;
    --white: #ffffff;
    --ink: #3a3a3a;
    --grey: #8a8a8a;
    --sky: #9fb6c9;
    --stone: #8d8272;
    --lawn: #7fa34a;
  }
  * { margin: 0; padding: 0; box-sizing: border-box; }
  html, body { width: 1200px; height: 848px; overflow: hidden; background: var(--white); }
  .flyer { position: relative; width: 1200px; height: 848px; font-family: "Open Sans", sans-serif; }

  .strip { position: absolute; left: 0; width: 1200px; height: 283px; overflow: hidden; }
  .strip--red { top: 0; background: var(--red); --text: var(--white); --accent: var(--navy); --feature: var(--white); }
  .strip--navy { top: 283px; background: var(--navy); --text: var(--white); --accent: var(--red); --feature: var(--white); }
  .strip--light { top: 566px; height: 282px; background: var(--mist); --text: var(--red); --accent: var(--navy); --feature: var(--red); }

  .agency-mark {
    position: absolute; left: 58px; top: 6px; width: 245px; height: 42px;
    background: var(--white); border: 2px solid #cfd5e0;
    display: flex; align-items: center; justify-content: center;
    font-weight: 600; font-size: 21px; color: var(--navy); letter-spacing: 0.5px;
  }

  .agent-photo {
    position: absolute; left: 50px; top: 70px; width: 248px; height: 163px;
    background: linear-gradient(160deg, #cdbf9c 0%, #8c7a5e 45%, #2a2528 100%);
    box-shadow: 0 2px 8px rgba(0,0,0,0.35);
  }

  .consultant-card {
    position: absolute; left: 462px; top: 6px; width: 275px; height: 84px;
    background: var(--white); text-align: center; padding-top: 18px;
  }
  .consultant-card__name { font-size: 19px; color: var(--ink); letter-spacing: 0.6px; line-height: 1; }
  .consultant-card__role { font-size: 11px; color: var(--grey); letter-spacing: 0.8px; margin-top: 4px; }
  .consultant-card__phone { font-size: 13px; color: var(--red); margin-top: 3px; }

  .pitch { position: absolute; left: 316px; top: 96px; color: var(--text); white-space: nowrap; }
  .pitch__line { display: block; }
  .pitch__lead { font-size: 36px; margin-left: 4px; line-height: 46px; }
  .pitch__call { font-size: 28px; line-height: 58px; margin-left: 8px; }
  .pitch__name { font-family: "Tinos", serif; font-weight: 700; font-size: 50px; color: var(--accent); margin: 0 14px 0 12px; }
  .pitch__tail { font-size: 29px; line-height: 40px; }

  .feature-title { position: absolute; left: 898px; top: 12px; font-size: 26px; color: var(--feature); }
  .feature-photo {
    position: absolute; left: 846px; top: 53px; width: 324px; height: 192px;
    border: 4px solid var(--white); box-shadow: 0 2px 8px rgba(0,0,0,0.3);
    background: linear-gradient(180deg, var(--sky) 0%, var(--stone) 40%, #6f675c 72%, var(--lawn) 100%);
  }
</style>
</head>
<body>
<main class="flyer">

  <section class="strip strip--red">
    <div class="agency-mark">KLT Homelink</div>
    <div class="agent-photo" role="img" aria-label="Portrait photo of Marisse Thornbury in uniform"></div>
    <div class="consultant-card">
      <p class="consultant-card__name">Marisse Thornbury</p>
      <p class="consultant-card__role">Sales Consultant</p>
      <p class="consultant-card__phone">0400 128 546</p>
    </div>
    <p class="pitch">
      <span class="pitch__line pitch__lead">"Are you considering selling?</span>
      <span class="pitch__line pitch__call">Call<span class="pitch__name">Marisse</span>today for a</span>
      <span class="pitch__line pitch__tail">complimentary market appraisal".</span>
    </p>
    <h2 class="feature-title">Feature Property</h2>
    <div class="feature-photo" role="img" aria-label="Photo of the featured stone house with gardens"></div>
  </section>

  <section class="strip strip--navy">
    <div class="agency-mark">KLT Homelink</div>
    <div class="agent-photo" role="img" aria-label="Portrait photo of Marisse Thornbury in uniform"></div>
    <div class="consultant-card">
      <p class="consultant-card__name">Marisse Thornbury</p>
      <p class="consultant-card__role">Sales Consultant</p>
      <p class="consultant-card__phone">0400 128 546</p>
    </div>
    <p class="pitch">
      <span class="pitch__line pitch__lead">"Are you considering selling?</span>
      <span class="pitch__line pitch__call">Call<span class="pitch__name">Marisse</span>today for a</span>
      <span class="pitch__line pitch__tail">complimentary market appraisal".</span>
    </p>
    <h2 class="feature-title">Feature Property</h2>
    <div class="feature-photo" role="img" aria-label="Photo of the featured stone house with gardens"></div>
  </section>

  <section class="strip strip--light">
    <div class="agency-mark">KLT Homelink</div>
    <div class="agent-photo" role="img" aria-label="Portrait photo of Marisse Thornbury in uniform"></div>
    <div class="consultant-card">
      <p class="consultant-card__name">Marisse Thornbury</p>
      <p class="consultant-card__role">Sales Consultant</p>
      <p class="consultant-card__phone">0400 128 546</p>
    </div>
    <p class="pitch">
      <span class="pitch__line pitch__lead">"Are you considering selling?</span>
      <span class="pitch__line pitch__call">Call<span class="pitch__name">Marisse</span>today for a</span>
      <span class="pitch__line pitch__tail">complimentary market appraisal".</span>
    </p>
    <h2 class="feature-title">Feature Property</h2>
    <div class="feature-photo" role="img" aria-label="Photo of the featured stone house with gardens"></div>
  </section>

</main>
</body>
</html>
```